Kereru Creative Harvest Fair

We are holding our inaugural event on the 21st October 2022 on the TerraStudia campus in Ashcombe Vale., from 10am until 2pm.The event will be a mix of Fourth year Food Technology students presenting their student projects and local producers show casing and educating around their products. The event is bought to you by CropNest along with Ashcombe Vale District Council and BRIX. The overall plan is to bring a spotlight to the amount of research and food related businesses are on this side of the river. The event will be free to enter and there will be food and products to purchase, but the main focus is on education.

```html
<!DOCTYPE html>
<html lang="en">
<head>
<meta charset="utf-8">
<title>Kereru Creative Harvest Fair</title>
<link href="https://fonts.googleapis.com/css2?family=Montserrat:wght@400;600;700;800&display=swap" rel="stylesheet">
<style>
  :root {
    --page: #ffffff;
    --frame: #c9c9c9;
    --cream: #fdf0c4;
    --sun: #f7d36a;
    --sky: #d9dccb;
    --deck: #b7a9d6;
    --grass: #2f9a5c;
    --grass-deep: #177a48;
    --ink: #333333;
    --orange: #f58a1f;
    --orange-deep: #ee6a12;
    --yellow: #f3e812;
    --white: #ffffff;
    --ring: #1f8f4f;
  }
  * { box-sizing: border-box; margin: 0; padding: 0; }
  html, body { width: 1200px; height: 1156px; overflow: hidden; background: var(--page); }
  body { font-family: "Montserrat", sans-serif; position: relative; }

  .sheet-frame {
    position: absolute; left: 3px; top: 3px; width: 1194px; height: 1150px;
    border: 1px solid var(--frame);
  }

  .poster {
    position: absolute; left: 228px; top: 120px; width: 715px; height: 891px;
    overflow: hidden;
  }
  .poster-backdrop {
    position: absolute; inset: 0;
    background: linear-gradient(180deg,
      var(--cream) 0%, var(--cream) 11%,
      var(--sun) 17%, #f4e39a 35%, var(--sky) 50%,
      #c9c6d8 58%, var(--deck) 64%, #8fb8a0 70%,
      var(--grass) 78%, var(--grass-deep) 100%);
  }

  .title-kicker {
    position: absolute; top: 22px; width: 100%; text-align: center;
    font-size: 33px; font-weight: 400; color: var(--ink); letter-spacing: 0.5px;
  }
  .title-main {
    position: absolute; top: 58px; width: 100%; text-align: center;
    font-size: 62px; font-weight: 800; color: var(--orange); letter-spacing: 1px;
    background: linear-gradient(180deg, var(--orange) 0%, var(--orange-deep) 100%);
    -webkit-background-clip: text; background-clip: text; -webkit-text-fill-color: transparent;
  }

  .dish-illustration {
    position: absolute; left: 138px; top: 168px; width: 434px; height: 212px;
    border-radius: 40px 40px 120px 120px;
    background: radial-gradient(ellipse at 50% 55%, #f2b36d 0%, #f08e6f 40%, rgba(94,190,170,0.55) 70%, rgba(247,211,106,0) 100%);
  }

  .event-date {
    position: absolute; top: 398px; width: 100%; text-align: center;
    font-size: 31px; font-weight: 800; color: var(--white);
  }
  .event-date .accent { color: var(--yellow); }
  .event-date sup { font-size: 16px; }

  .event-time {
    position: absolute; left: 183px; top: 446px; width: 350px; height: 36px;
    border-top: 2px solid var(--white); border-bottom: 2px solid var(--white);
    display: flex; align-items: center; justify-content: center; gap: 10px;
    font-size: 21px; font-weight: 700; color: var(--white);
  }
  .event-time .label { color: var(--yellow); padding-right: 10px; border-right: 2px solid var(--white); }
  .event-time .accent { color: var(--yellow); }

  .event-venue {
    position: absolute; top: 506px; width: 100%; text-align: center;
    font-size: 24px; font-weight: 800; color: var(--yellow); line-height: 36px;
  }

  .highlight {
    position: absolute; top: 609px; width: 150px; margin-left: -75px; text-align: center;
  }
  .highlight-photo {
    width: 108px; height: 108px; margin: 0 auto; border-radius: 50%;
    border: 5px solid var(--ring);
  }
  .highlight-label {
    margin-top: 10px; font-size: 13px; font-weight: 700; color: var(--white); line-height: 18px;
  }
  .h1 { left: 96px; }  .h1 .highlight-photo { background: linear-gradient(135deg, #6d86a8, #d8c6b4); }
  .h2 { left: 260px; } .h2 .highlight-photo { background: linear-gradient(135deg, #e9eef2, #b9c2cc); }
  .h3 { left: 423px; } .h3 .highlight-photo { background: linear-gradient(135deg, #f2f2f0, #c8b8a6); }
  .h4 { left: 584px; } .h4 .highlight-photo { background: linear-gradient(135deg, #e6c23a, #8aa25a); }

  .sponsor-intro {
    position: absolute; top: 803px; width: 100%; text-align: center;
    font-size: 10px; font-weight: 700; color: var(--white); letter-spacing: 0.5px;
  }
  .sponsor {
    position: absolute; top: 826px; text-align: center; color: var(--white);
    font-weight: 800;
  }
  .sponsor-crop { left: 150px; font-size: 26px; }
  .sponsor-council { left: 280px; width: 170px; top: 826px; font-size: 13px; line-height: 15px; }
  .sponsor-brix { left: 478px; font-size: 28px; }
</style>
</head>
<body>
  <div class="sheet-frame"></div>

  <main class="poster">
    <div class="poster-backdrop" role="img" aria-label="Photo of a lit pedestrian bridge under a warm sky leading onto green lawn"></div>

    <p class="title-kicker">KERERU CREATIVE</p>
    <h1 class="title-main">HARVEST FAIR</h1>

    <div class="dish-illustration" role="img" aria-label="Illustration of three bowls of food with noodles, dumplings and salad"></div>

    <p class="event-date"><span class="accent">21<sup>st</sup></span> OCTOBER <span class="accent">2022</span></p>
    <p class="event-time"><span class="label">TIME</span><span>At Sharp <span class="accent">10:00</span> AM</span></p>
    <p class="event-venue">TerraStudia Campus<br>In Ashcombe Vale</p>

    <div class="highlight h1">
      <div class="highlight-photo" role="img" aria-label="Photo of students preparing products at a workbench"></div>
      <p class="highlight-label">PRODUCT<br>PREPARATION</p>
    </div>
    <div class="highlight h2">
      <div class="highlight-photo" role="img" aria-label="Photo of a student in a lab coat presenting research"></div>
      <p class="highlight-label">STUDENT'S<br>PRESENTATION</p>
    </div>
    <div class="highlight h3">
      <div class="highlight-photo" role="img" aria-label="Photo of a chef in whites giving a demonstration"></div>
      <p class="highlight-label">CHEF'S<br>DEMONSTRATION</p>
    </div>
    <div class="highlight h4">
      <div class="highlight-photo" role="img" aria-label="Photo of colourful food trucks parked in a row"></div>
      <p class="highlight-label">FOOD TRUCKS<br>FOR LUNCH</p>
    </div>

    <p class="sponsor-intro">THE EVENT IS BROUGHT TO YOU BY</p>
    <p class="sponsor sponsor-crop">CropNest</p>
    <p class="sponsor sponsor-council">ASHCOMBE VALE<br>DISTRICT COUNCIL</p>
    <p class="sponsor sponsor-brix">BRIX</p>
  </main>
</body>
</html>
```